Web Design Project for NFYL

Hi,
I am looking for a website design for the Northern Federation of Youth Listeners.
This is an organisation which helps with legal disputes and other challenges which involve children.  The company want a web page which is professional but friendly.  The purpose of the website is to explain what the organisation does and to give people a place where they can download documents and information.
The homepage will have a video on the page.  ALSO, we would prefer the site to have a left hand navigation (not a top navigation).
I have enclosed the logo, a picture of the old (rubbish) home page and a screenshot from the video (you are welcome to change the dimensions).
If you have any questions, please ask.
-D
UPDATE: 6th DECEMBER:
Thanks for the designs so far.  I promise to give feedback to every single person.  In the meantime, can I just say that there's some good designs so far but I don't think anyone has nailed this yet.
So, I am uploading a screenshot called "theylikethis.jpg".  This is a screenshot from a website that the client says they like.
Can I also say, it's okay to reduce the size of the video.  I'm seeing a lot of massive videos.
Thanks folks!
UPDATE:  You can view a live demo of the site that they like at www.demohostqv.co.uk
UPDATE:  I've just found another good example of a site with a left nav at www.brightpathresourcehub.com

Updates
Hi,
Hi folks,
Had a quick look at the designs and just to say how impressed I am with the qualityand choice. There are a few that caught my eye and I'll try and narrow them down.I've also passed the link onto the other representatives for their input beforemaking a final choice. If I don't hear from any of the other represenatatives by Wednesday, I'll chose adesign and let you know. Once again many thanks for the quick response in gettingdesigns done and really looking forward to seeing the completed website.
Industry/Entity Type
Legal
Requirements
Must have
- a video player (any size of your choosing)
a left side navigation
the logo

```html
<!DOCTYPE html>
<html lang="en">
<head>
<meta charset="utf-8">
<title>NFYL – Northern Federation of Youth Listeners</title>
<link rel="stylesheet" href="https://fonts.googleapis.com/css2?family=Lato:wght@300;400;700&family=Oswald:wght@500&display=swap">
<style>
:root{
  --brand:#0b3f9c;
  --brand-deep:#08358a;
  --bg-edge:#1e4ea6;
  --bg-mid:#6a8fd2;
  --ink:#1a1a1a;
  --rule:#0b3f9c;
  --white:#ffffff;
  --muted:#444;
}
*{box-sizing:border-box;margin:0;padding:0}
html,body{width:1140px;height:1200px;overflow:hidden}
body{background:radial-gradient(ellipse at 50% 55%,var(--bg-mid) 0%,#3e6cc0 45%,var(--bg-edge) 100%);font-family:'Lato',sans-serif;color:var(--ink)}
.stage{position:absolute;left:0;top:0;width:1368px;height:1440px;transform:scale(.83333);transform-origin:0 0}
.page{position:absolute;left:194px;top:0;width:980px;height:1398px;background:var(--white);box-shadow:0 0 18px rgba(0,0,0,.25)}
.abs{position:absolute}
.logo{left:23px;top:0;width:154px;height:166px;background:var(--brand);display:flex;align-items:center;justify-content:center;color:var(--white);font-size:34px;font-weight:400;letter-spacing:1px}
.callout{left:742px;top:0;width:217px;height:80px;background:var(--brand);color:var(--white);text-align:center;padding-top:19px}
.callout small{display:block;font-size:15px;font-weight:300}
.callout strong{display:block;font-size:21px;font-weight:700;margin-top:1px}
.site-title{left:197px;top:96px;font-size:37px;line-height:37px;font-weight:700;color:var(--brand);letter-spacing:-.3px}
.side-nav{left:22px;top:198px;width:154px;list-style:none}
.side-nav li{height:36px;border-bottom:2px solid var(--rule);display:flex;align-items:center;justify-content:center;font-size:15px;font-weight:300;color:var(--brand)}
.side-nav li.active{background:var(--brand);color:var(--white);font-weight:700;height:32px;border-top:2px solid var(--rule);box-shadow:0 0 0 0 var(--white), inset 0 -2px 0 var(--white)}
.video{left:199px;top:198px;width:543px;height:302px;background:#000;box-shadow:0 10px 18px rgba(0,0,0,.25)}
.video-still{position:absolute;left:0;top:0;width:504px;height:273px;background:linear-gradient(160deg,#2f5a1a 0%,#6ea33a 45%,#9ac64e 70%,#557d2a 100%)}
.video-tools{position:absolute;right:6px;top:6px;display:flex;flex-direction:column;gap:6px}
.video-tools span{width:22px;height:18px;background:#222;border-radius:2px}
.video-bar{position:absolute;left:0;bottom:0;width:100%;height:29px;background:#111;display:flex;align-items:center;padding:0 8px}
.video-bar .play{width:26px;height:22px;background:#2a2a2a;display:flex;align-items:center;justify-content:center}
.video-bar .track{flex:1;height:6px;margin:0 10px 0 16px;border:1px solid #666;border-radius:3px}
.video-bar .hd{color:#39b3ff;font-size:10px;font-weight:700;margin-right:6px}
.person{left:766px;width:190px}
.person .avatar{width:68px;height:62px;background:linear-gradient(135deg,#e8b48c,#b9744c)}
.person h4{font-size:13px;font-weight:700;margin-top:6px}
.person p{font-size:10px;color:var(--muted)}
.content{left:198px;top:536px;width:545px}
.content h2{font-size:23px;font-weight:400;line-height:28px;color:#111}
.content p{font-size:13px;line-height:17px;margin-top:15px}
.content h2 + p{margin-top:15px}
.content p + h2{margin-top:14px}
.content .divider{border-top:2px dotted #777;margin:23px 0 18px 4px}
.content .more{display:inline-block;margin-top:14px;font-size:14px;font-weight:700;color:var(--brand);text-decoration:underline;margin-left:-2px}
.promo{left:764px;width:194px;background:linear-gradient(180deg,#1a4fb0,var(--brand-deep));color:var(--white);text-align:center}
.help{top:551px;height:165px;padding-top:12px}
.help h3{font-size:29px;font-weight:700;line-height:36px}
.help p{font-size:25px;font-weight:300;line-height:29px}
.help a{display:block;margin-top:18px;font-size:18px;color:var(--white);text-decoration:none}
.download{top:736px;height:165px;padding-top:8px}
.download h3{font-size:30px;font-weight:700;line-height:36px}
.download p{font-size:15px;font-weight:300;line-height:19px}
.doc-tile{width:48px;height:56px;background:#d4121a;margin:12px auto 0;border-radius:3px}
.social{top:921px;height:215px;text-align:left;padding:12px 0 0 8px}
.social-row{display:flex;gap:8px}
.social-row + .social-row{margin-top:16px}
.social-icon{width:38px;height:38px;background:#dfe7f5;border-radius:5px;flex:none}
.social h3{font-family:'Oswald',sans-serif;font-size:18px;font-weight:500;line-height:22px}
.social p{font-size:12px;line-height:15px;margin-top:2px}
.social .btns{display:flex;gap:12px;margin-top:8px;align-items:center}
.social .btn{background:#eef1f7;color:#3b5998;font-size:11px;padding:2px 6px;border:1px solid #ccd}
.social .count{background:var(--white);color:#222;font-size:14px;padding:2px 8px;border:1px solid #ccd}
.social .count.big{font-weight:700;color:var(--brand);font-size:15px;padding:2px 12px}
.footer{left:0;top:1361px;width:980px;height:37px;border-top:1px solid #aaa}
.footer .copy{position:absolute;left:38px;top:10px;font-family:Arial,sans-serif;font-size:12px}
.footer ul{position:absolute;right:38px;top:13px;list-style:none;display:flex;gap:17px;font-family:Arial,sans-serif;font-size:11px}
</style>
</head>
<body>
<div class="stage">
  <div class="page">
    <div class="abs logo">NFYL</div>
    <div class="abs callout"><small>Free Legal Advice</small><strong>Call: 0800 555 0190</strong></div>
    <h1 class="abs site-title">Northern Federation of<br>Youth Listeners</h1>

    <ul class="abs side-nav">
      <li class="active">HOME</li>
      <li>ABOUT US</li>
      <li>NEWS</li>
      <li>CONFERENCES</li>
      <li>MINTES</li>
      <li>ANNUAL REPORT</li>
      <li>ARCHIVE</li>
      <li>CONTACT US</li>
      <li>LINKS</li>
    </ul>

    <div class="abs video">
      <div class="video-still" role="img" aria-label="Video still: a young child sitting on grass beside a tree"></div>
      <div class="video-tools"><span></span><span></span><span></span></div>
      <div class="video-bar">
        <div class="play"><svg width="10" height="12" viewBox="0 0 10 12"><path d="M0 0L10 6L0 12Z" fill="#fff"/></svg></div>
        <div class="track"></div>
        <span class="hd">HD</span>
      </div>
    </div>

    <div class="abs person" style="top:202px">
      <div class="avatar" role="img" aria-label="Portrait photo of a team member"></div>
      <h4>Lorem Ipsum is simply</h4>
      <p>Lorem Ipsum is simply</p>
    </div>
    <div class="abs person" style="top:313px">
      <div class="avatar" role="img" aria-label="Portrait photo of a team member" style="background:linear-gradient(135deg,#c99070,#6b3f2a)"></div>
      <h4>Lorem Ipsum is simply</h4>
      <p>Lorem Ipsum is simply</p>
    </div>

    <div class="abs content">
      <h2>Welcome to&nbsp; NFYL...</h2>
      <p>Lorem Ipsum is simply dummy text of the printing and typesetting industry. Lorem Ipsum has been the industry's standard dummy text ever since the 1500s, when an unknown printer took a galley of type and scrambled it to make a type specimen book. It has survived not only five centuries, but also the leap into electronic typesetting, remaining essentially unchanged. It was popularised in the 1960s with the release of Typesheet sheets containing Lorem Ipsum passages, and more recently with desktop publishing software like Quillset Composer including versions of Lorem Ipsum.</p>
      <p>Lorem Ipsum is simply dummy text of the printing and typesetting industry. Lorem Ipsum has been the industry's standard dummy text ever since the 1500s, when an unknown printer took a galley of type and scrambled it to make a type specimen book. It has survived not only five centuries, but also the leap into electronic typesetting, remaining essentially unchanged.</p>
      <p>Lorem Ipsum has been the industry's standard dummy text ever since the 1500s, when an unknown printer took a galley of type and scrambled it to make a type specimen book. It has survived not only five centuries.</p>
      <h2>Why Was The NFYL FORMED?</h2>
      <p>Lorem Ipsum is simply dummy text of the printing and typesetting industry. Lorem Ipsum has been the industry's standard dummy text ever since the 1500s, when an unknown printer took a galley of type and scrambled it to make a type specimen book. It has survived not only five centuries, but also the leap into electronic typesetting, remaining essentially unchanged.</p>
      <h2>Objectives</h2>
      <p>Lorem Ipsum has been the industry's standard dummy text ever since the 1500s, when an unknown printer took a galley of type and scrambled it to make a type specimen book.</p>
      <div class="divider"></div>
      <h2>Latest news</h2>
      <p>Lorem Ipsum has been the industry's standard dummy text ever since the 1500s, when an unknown printer took a galley of type and scrambled it to make a type specimen book.</p>
      <a class="more" href="#">READ MORE </a>
      <h2 style="margin-top:18px">Legal updates</h2>
      <p>Lorem Ipsum has been the industry's standard dummy text ever since the 1500s, when an unknown printer took a galley of type and scrambled it to make a type specimen book.</p>
    </div>

    <div class="abs promo help">
      <h3>Need help?</h3>
      <p>Ask us legal<br>Question.</p>
      <a href="#">Click to Email</a>
    </div>
    <div class="abs promo download">
      <h3>Download</h3>
      <p>Legal Documents<br>and information</p>
      <div class="doc-tile"></div>
    </div>
    <div class="abs promo social">
      <div class="social-row">
        <div class="social-icon"></div>
        <div>
          <h3>We're on Linkbook</h3>
          <p>Like us to see our daily<br>updates!</p>
          <div class="btns"><span class="btn">Like</span><span class="count">20</span></div>
        </div>
      </div>
      <div class="social-row">
        <div class="social-icon"></div>
        <div>
          <h3>We're on Chirper</h3>
          <p>Like us to see our daily<br>updates!</p>
          <div class="btns"><span class="btn">Share</span><span class="count big">241</span></div>
        </div>
      </div>
    </div>

    <div class="abs footer">
      <span class="copy">Copyright © 2012&nbsp; The NFYL</span>
      <ul>
        <li>Home</li><li>About Us</li><li>News</li><li>Conferences</li><li>Mintes</li><li>Annual Report</li><li>Archive</li><li>Contact Us</li><li>Links</li>
      </ul>
    </div>
  </div>
</div>
</body>
</html>
```